Corvane Lift Inc Website Deisgn

We are a new small elevator contracting company.
We would like a full website designed similar to
http://pellusk-lifts.example or https://www.marbolt-hoistworks.example/
In addition to contents found on the above webpages.. we would like a section for project gallery etc.... have fun with it ... make it professional

Target Market(s)

Elevator Consultants - Property managers - Condo Boards - Commercial office buildings

Coding

Coded - Design and coding required

Number of Pages Required

5+ page

Requirements
Must have
• Navigation Bar.. Be view able via mobile ..Should be pictures of Tall Office buildings in background.. Toronto city skyline etc....

Have Fun!

```html
<!DOCTYPE html>
<html lang="en">
<head>
<meta charset="utf-8">
<title>Corvane Lift Inc — Website Design</title>
<link href="https://fonts.googleapis.com/css2?family=Oswald:wght@500;600;700&family=Open+Sans:wght@400;600;700&display=swap" rel="stylesheet">
<style>
:root{
  --red:#c8202f;
  --red-dark:#a51624;
  --navy:#1f2233;
  --navy-deep:#161827;
  --ink:#1c1c22;
  --muted:#6b6e78;
  --line:#e3e4e8;
  --paper:#ffffff;
  --foot-text:#c9cbd4;
  --sky-a:#0d1326;
  --sky-b:#2a3556;
  --sky-c:#5a4a3e;
}
*{margin:0;padding:0;box-sizing:border-box}
html,body{width:1200px;height:2424px;overflow:hidden;background:var(--paper)}
body{position:relative;font-family:"Open Sans",Arial,sans-serif;color:var(--ink)}
.brand{display:flex;align-items:center;gap:10px;font-family:"Oswald",Arial,sans-serif;font-weight:700;color:var(--ink);text-transform:uppercase;letter-spacing:.5px;white-space:nowrap}
.brand-dot{border-radius:50%;background:var(--ink);flex:none}
.brand.light{color:#fff}
.brand.light .brand-dot{background:#fff}
.board-title{position:absolute;left:0;top:240px;width:1200px;display:flex;justify-content:center}
.board-title .brand{font-size:62px;gap:22px}
.board-title .brand-dot{width:64px;height:64px}

.screen{position:absolute;background:#fff;overflow:hidden;box-shadow:0 2px 12px rgba(0,0,0,.14)}
.abs{position:absolute}
.photo{position:absolute}
.sky{background:linear-gradient(180deg,var(--sky-a) 0%,var(--sky-b) 55%,var(--sky-c) 100%)}
.heading{font-family:"Oswald",Arial,sans-serif;font-weight:600;color:var(--ink);text-align:center}
.small{color:var(--muted);text-align:center}
.btn{background:var(--red);color:#fff;font-weight:600;display:flex;align-items:center;justify-content:center;border-radius:2px}
.card-label{font-family:"Oswald",Arial,sans-serif;font-weight:600;text-align:center;color:var(--ink)}
.field{background:#fff;border:1px solid var(--line);border-radius:2px}

/* Desktop */
.desktop{left:348px;top:380px;width:780px;height:2012px}
.d-nav{left:0;top:0;width:780px;height:40px;display:flex;align-items:center;padding:0 24px}
.d-nav .brand{font-size:13px;gap:5px}
.d-nav .brand-dot{width:13px;height:13px}
.d-links{display:flex;gap:20px;margin-left:auto;margin-right:16px;font-size:7px;color:var(--ink)}
.d-nav .btn{font-size:7px;width:68px;height:18px}
.d-hero{left:0;top:40px;width:780px;height:380px}
.d-hero-copy{left:104px;top:170px;width:320px;color:#fff}
.d-hero-copy .kicker{font-size:7px;font-weight:700;letter-spacing:.6px;text-transform:uppercase;margin-bottom:6px}
.d-hero-copy h1{font-family:"Oswald",Arial,sans-serif;font-size:22px;line-height:1.2;font-weight:600}
.d-hero-copy .btn{width:58px;height:16px;font-size:6.5px;margin-top:10px}
.d-form{left:476px;top:96px;width:200px;height:270px;background:#fff;box-shadow:0 3px 10px rgba(0,0,0,.18);padding:0 14px 14px}
.form-head{background:var(--red);color:#fff;font-family:"Oswald",Arial,sans-serif;font-weight:600;text-align:center;margin:0 -14px 14px}
.d-form .form-head{height:34px;line-height:34px;font-size:11px}
.d-form .field{height:20px;margin-bottom:9px;font-size:6px;color:var(--muted);padding:5px 6px}
.d-form .field.tall{height:64px}
.d-form .btn{height:20px;font-size:7px}
.d-services-title{left:0;top:446px;width:780px;font-size:22px}
.d-services-sub{left:220px;top:482px;width:340px;font-size:6px;line-height:1.6}
.d-card{position:absolute;width:280px;height:222px;background:#fff;box-shadow:0 2px 8px rgba(0,0,0,.1)}
.d-card .photo{left:0;top:0;width:280px;height:180px}
.d-card .card-label{position:absolute;left:0;top:190px;width:280px;font-size:11px}
.d-gallery-title{left:0;top:1074px;width:780px;font-size:20px}
.d-gallery-sub{left:220px;top:1106px;width:340px;font-size:6px;line-height:1.6}
.d-gallery{left:0;top:1168px;width:780px;height:300px;display:flex}
.d-gallery .photo{position:relative;height:100%}
.d-footer{left:0;top:1560px;width:780px;height:452px;background:var(--navy);color:#fff}
.d-ask{left:104px;top:1514px;width:572px;height:92px;background:var(--red);display:flex;align-items:center;padding:0 28px}
.d-ask h2{font-family:"Oswald",Arial,sans-serif;color:#fff;font-size:17px;font-weight:600}
.d-ask .field{margin-left:auto;width:110px;height:18px;font-size:6px;color:var(--muted);padding:4px 6px}
.d-ask .btn{width:50px;height:18px;font-size:6.5px;background:var(--navy);margin-left:4px}
.d-foot-cols{left:104px;top:1660px;width:600px;display:flex;gap:28px;color:#fff}
.d-foot-brand .brand{font-size:16px;gap:6px}
.d-foot-brand .brand-dot{width:16px;height:16px}
.about-box{background:#fff;color:var(--ink);margin-top:12px;padding:8px}
.about-box b{display:block;font-size:7px;margin-bottom:4px}
.about-box p{font-size:5.5px;line-height:1.6;color:var(--muted)}
.col h4{font-family:"Oswald",Arial,sans-serif;font-weight:600;font-size:9px;margin-bottom:8px;color:#fff}
.col li{list-style:none;font-size:6px;line-height:2.1;color:var(--foot-text)}
.contact li{display:flex;align-items:center;gap:5px}
.ico{width:9px;height:9px;border-radius:50%;background:var(--red);flex:none;display:flex;align-items:center;justify-content:center}
.d-copy{left:104px;top:1968px;width:572px;display:flex;justify-content:space-between;font-size:5.5px;color:#a9acb8}

/* Mobile */
.mobile{left:72px;top:388px;width:216px;height:2004px}
.m-nav{left:0;top:0;width:216px;height:22px;display:flex;align-items:center;padding:0 8px}
.m-nav .brand{font-size:7px;gap:3px}
.m-nav .brand-dot{width:7px;height:7px}
.burger{margin-left:auto;width:14px;height:11px;background:var(--red);display:flex;flex-direction:column;justify-content:center;gap:1.5px;padding:0 3px}
.burger i{display:block;height:1px;background:#fff}
.m-hero{left:0;top:22px;width:216px;height:230px}
.m-hero-copy{left:12px;top:40px;width:192px;color:#fff}
.m-hero-copy .kicker{font-size:4.5px;font-weight:700;text-transform:uppercase;margin-bottom:4px}
.m-hero-copy h1{font-family:"Oswald",Arial,sans-serif;font-size:12px;line-height:1.2;font-weight:600}
.m-form{left:16px;top:150px;width:184px;height:242px;background:#fff;box-shadow:0 2px 8px rgba(0,0,0,.2);padding:0 12px 12px}
.m-form .form-head{height:26px;line-height:26px;font-size:8px;margin:0 -12px 12px}
.m-form .field{height:17px;margin-bottom:8px;font-size:5px;color:var(--muted);padding:4px 5px}
.m-form .field.tall{height:48px}
.m-form .btn{height:16px;font-size:5.5px}
.m-title{left:0;width:216px;font-size:12px}
.m-sub{left:24px;width:168px;font-size:4.5px;line-height:1.6}
.m-photo{left:40px;width:136px;height:110px}
.m-label{left:0;width:216px;font-size:8px}
.m-ask{left:16px;top:1340px;width:184px;height:72px;background:var(--red);padding:10px;text-align:center}
.m-ask h2{font-family:"Oswald",Arial,sans-serif;color:#fff;font-size:9px;font-weight:600;margin-bottom:8px}
.m-ask .row{display:flex;gap:3px}
.m-ask .field{flex:1;height:14px;font-size:4.5px;color:var(--muted);padding:3px 4px;text-align:left}
.m-ask .btn{width:38px;height:14px;font-size:5px;background:var(--navy)}
.m-footer{left:0;top:1376px;width:216px;height:628px;background:var(--navy);color:#fff;padding:56px 16px 0}
.m-footer .brand{font-size:12px;gap:4px;justify-content:center}
.m-footer .brand-dot{width:12px;height:12px}
.m-footer .about-box{margin:12px 20px 24px}
.m-cols{display:flex;gap:30px;margin-bottom:24px}
.m-footer .col h4{font-size:7px}
.m-footer .col li{font-size:5px}
.m-copy{font-size:4.5px;color:#a9acb8;text-align:center;margin-top:28px;line-height:1.8}
</style>
</head>
<body>

<header class="board-title">
  <div class="brand"><span class="brand-dot"></span>Corvane Lift Inc</div>
</header>

<!-- Desktop home page -->
<section class="screen desktop">
  <nav class="abs d-nav">
    <div class="brand"><span class="brand-dot"></span>Corvane Lift Inc</div>
    <div class="d-links"><span>Home</span><span>Our Services</span><span>Modernization</span><span>Gallery</span><span>Video Gallery</span><span>Careers</span></div>
    <div class="btn">Contact Now</div>
  </nav>
  <div class="photo sky d-hero" role="img" aria-label="Toronto skyline of tall office towers at night"></div>
  <div class="abs d-hero-copy">
    <p class="kicker">We are Toronto's Elevator Experts</p>
    <h1>Elevator Maintenance, Repair &amp; Modernization</h1>
    <div class="btn">Learn More</div>
  </div>
  <form class="abs d-form">
    <div class="form-head">Have Questions?</div>
    <div class="field">Full Name</div>
    <div class="field">Email Address</div>
    <div class="field">Phone Number</div>
    <div class="field tall">Your Message</div>
    <div class="btn">Send Message</div>
  </form>

  <h2 class="abs heading d-services-title">Services We Offer</h2>
  <p class="abs small d-services-sub">We keep your building moving with safe, reliable elevator service for condos, offices and commercial towers across the city.</p>
  <div class="d-card" style="left:104px;top:530px"><div class="photo" style="background:linear-gradient(135deg,#3a2a1c,#d08a2c 55%,#2b2320)" role="img" aria-label="Technician modernizing elevator machinery"></div><div class="card-label">Modernization</div></div>
  <div class="d-card" style="left:396px;top:530px"><div class="photo" style="background:linear-gradient(135deg,#6a8fa3,#c9d6de 50%,#47606e)" role="img" aria-label="Technician maintaining an elevator shaft"></div><div class="card-label">Maintenance</div></div>
  <div class="d-card" style="left:104px;top:782px"><div class="photo" style="background:linear-gradient(135deg,#1d3a55,#7fa9c2 50%,#2e4456)" role="img" aria-label="Glass elevator being repaired"></div><div class="card-label">Repairing</div></div>
  <div class="d-card" style="left:396px;top:782px"><div class="photo" style="background:linear-gradient(135deg,#2a2a2e,#b6202c 50%,#3b3b40)" role="img" aria-label="Red hand tools on a workbench"></div><div class="card-label">Other Services</div></div>

  <h2 class="abs heading d-gallery-title">Our Project Gallery</h2>
  <p class="abs small d-gallery-sub">A look at recent installations and modernization projects we completed in office towers and condos.</p>
  <div class="abs d-gallery">
    <div class="photo" style="width:130px;background:linear-gradient(180deg,#2d6db0,#9cc3e3)" role="img" aria-label="Glass office tower against blue sky"></div>
    <div class="photo" style="width:150px;background:linear-gradient(180deg,#8fb0cc,#3c4b5c)" role="img" aria-label="Downtown office buildings"></div>
    <div class="photo" style="width:120px;background:linear-gradient(180deg,#c9b8a0,#6d5e50)" role="img" aria-label="Stone high-rise facade"></div>
    <div class="photo" style="width:130px;background:linear-gradient(180deg,#3d4450,#1c2028)" role="img" aria-label="Dark glass skyscraper"></div>
    <div class="photo" style="width:130px;background:linear-gradient(180deg,#6fa3d6,#2f4d6d)" role="img" aria-label="Tower looking up to the sky"></div>
    <div class="photo" style="width:120px;background:linear-gradient(180deg,#e2a246,#2d4f7a)" role="img" aria-label="Modern tower with warm sunlight"></div>
  </div>

  <div class="abs d-footer"></div>
  <div class="abs d-ask">
    <h2>Do You Have A Question?</h2>
    <div class="field">Enter your email</div>
    <div class="btn">Submit</div>
  </div>
  <div class="abs d-foot-cols">
    <div class="d-foot-brand" style="width:170px">
      <div class="brand light"><span class="brand-dot"></span>Corvane Lift Inc</div>
      <div class="about-box"><b>About Us</b><p>Corvane Lift Inc is a Toronto elevator contractor serving property managers, condo boards and offices.</p></div>
    </div>
    <div class="col" style="width:100px"><h4>Quick Links</h4><ul><li>Home</li><li>Our Services</li><li>Gallery</li><li>Careers</li><li>Contact Us</li></ul></div>
    <div class="col" style="width:100px"><h4>Others</h4><ul><li>Free Quote</li><li>Pricing</li><li>Consulting</li></ul></div>
    <div class="col contact"><h4>Contact Info</h4><ul>
      <li><span class="ico"><svg width="5" height="5" viewBox="0 0 10 10"><path d="M2 1l2 2-1 1.5c.8 1.5 1.8 2.5 3.3 3.3L7.8 6.8 10 8.5 8.5 10C4.5 10 0 5.5 0 1.5z" fill="#fff"/></svg></span>(416) 555-0148</li>
      <li><span class="ico"><svg width="5" height="5" viewBox="0 0 10 10"><rect x="0" y="2" width="10" height="6" fill="#fff"/></svg></span>info@corvanelift.example</li>
      <li><span class="ico"><svg width="5" height="5" viewBox="0 0 10 10"><path d="M5 0a3.5 3.5 0 0 0-3.5 3.5C1.5 6 5 10 5 10s3.5-4 3.5-6.5A3.5 3.5 0 0 0 5 0z" fill="#fff"/></svg></span>88 Halvern Ave, Toronto</li>
    </ul></div>
  </div>
  <div class="abs d-copy"><span>Privacy Policy · Terms</span><span>© Copyright 2024 Corvane Lift Inc. All rights reserved.</span></div>
</section>

<!-- Mobile home page -->
<section class="screen mobile">
  <nav class="abs m-nav">
    <div class="brand"><span class="brand-dot"></span>Corvane Lift Inc</div>
    <div class="burger"><i></i><i></i><i></i></div>
  </nav>
  <div class="photo sky m-hero" role="img" aria-label="Toronto skyline of tall office towers at night"></div>
  <div class="abs m-hero-copy">
    <p class="kicker">We are Toronto's Elevator Experts</p>
    <h1>Elevator Maintenance Repair &amp; Modernization</h1>
  </div>
  <form class="abs m-form">
    <div class="form-head">Have Questions?</div>
    <div class="field">Full Name</div>
    <div class="field">Email Address</div>
    <div class="field">Phone Number</div>
    <div class="field tall">Your Message</div>
    <div class="btn">Send Message</div>
  </form>

  <h2 class="abs heading m-title" style="top:412px">Services We Offer</h2>
  <p class="abs small m-sub" style="top:436px">Safe, reliable elevator service for condos, offices and commercial towers across the city.</p>
  <div class="photo m-photo" style="top:480px;background:linear-gradient(135deg,#3a2a1c,#d08a2c 55%,#2b2320)" role="img" aria-label="Technician modernizing elevator machinery"></div>
  <div class="abs card-label m-label" style="top:598px">Modernization</div>
  <div class="photo m-photo" style="top:640px;background:linear-gradient(135deg,#6a8fa3,#c9d6de 50%,#47606e)" role="img" aria-label="Technician maintaining an elevator shaft"></div>
  <div class="abs card-label m-label" style="top:758px">Maintenance</div>
  <div class="photo m-photo" style="top:800px;background:linear-gradient(135deg,#1d3a55,#7fa9c2 50%,#2e4456)" role="img" aria-label="Glass elevator being repaired"></div>
  <div class="abs card-label m-label" style="top:918px">Repairing</div>
  <div class="photo m-photo" style="top:960px;background:linear-gradient(135deg,#2a2a2e,#b6202c 50%,#3b3b40)" role="img" aria-label="Red hand tools on a workbench"></div>
  <div class="abs card-label m-label" style="top:1078px">Other Services</div>

  <h2 class="abs heading m-title" style="top:1126px">Our Project Gallery</h2>
  <p class="abs small m-sub" style="top:1150px">Recent installations and modernization projects.</p>
  <div class="photo" style="left:0;top:1176px;width:216px;height:150px;background:linear-gradient(90deg,#2d6db0,#8fb0cc 40%,#3d4450 70%,#e2a246)" role="img" aria-label="Office towers in downtown Toronto"></div>

  <div class="abs m-footer">
    <div class="brand light"><span class="brand-dot"></span>Corvane Lift Inc</div>
    <div class="about-box"><b>About Us</b><p>Corvane Lift Inc is a Toronto elevator contractor serving property managers, condo boards and offices.</p></div>
    <div class="m-cols">
      <div class="col"><h4>Quick Links</h4><ul><li>Home</li><li>Our Services</li><li>Gallery</li><li>Careers</li><li>Contact Us</li></ul></div>
      <div class="col"><h4>Others</h4><ul><li>Free Quote</li><li>Pricing</li><li>Consulting</li></ul></div>
    </div>
    <div class="col contact"><h4>Contact Info</h4><ul>
      <li><span class="ico"></span>(416) 555-0148</li>
      <li><span class="ico"></span>info@corvanelift.example</li>
      <li><span class="ico"></span>88 Halvern Ave, Toronto</li>
    </ul></div>
    <p class="m-copy">© Copyright 2024 Corvane Lift Inc.<br>All rights reserved.</p>
  </div>
  <div class="abs m-ask">
    <h2>Do You Have A Question?</h2>
    <div class="row"><div class="field">Enter your email</div><div class="btn">Submit</div></div>
  </div>
</section>

</body>
</html>
```